Business Card Design Project

Hello
I want a Simple Business card that uses the company logo that is easily reasonable but looks professional as I am an IT Services company and would look to share these cards with prospective clients.
The details are:
Kestrel Arc Solutions
14 Morrow Lane
Birmingham
B7 4QX
Telephone 0845 217 6640
I would like my name Oliver Hastings and my title Director on the card.
Target Market(s)
IT Professionals
Industry/Entity Type
Business

```html
<!DOCTYPE html>
<html lang="en">
<head>
<meta charset="utf-8">
<title>Kestrel Arc Solutions – Business Card</title>
<link href="https://fonts.googleapis.com/css2?family=Open+Sans:wght@400;600;700&display=swap" rel="stylesheet">
<style>
  :root {
    --bg: #ecebe7;
    --green-light: #c9e27e;
    --green: #9fcd4a;
    --green-deep: #7fb935;
    --ink: #2b2b2b;
    --ink-soft: #4a4a4a;
    --paper: #ffffff;
    --leaf-wash: #e8f1d6;
  }
  * { box-sizing: border-box; margin: 0; padding: 0; }
  html, body {
    width: 1200px; height: 900px; overflow: hidden;
    background: var(--bg);
    font-family: "Open Sans", Arial, sans-serif;
  }
  .sheet {
    position: relative; width: 1200px; height: 900px;
    display: flex; flex-direction: column; align-items: center; justify-content: center; gap: 40px;
  }
  .card {
    position: relative; width: 700px; height: 400px; overflow: hidden;
    box-shadow: 0 6px 18px rgba(0,0,0,0.18);
  }
  /* Front */
  .card--front {
    background: linear-gradient(160deg, var(--green-light) 0%, var(--green) 55%, var(--green-deep) 100%);
    display: flex; align-items: center; justify-content: center; gap: 14px;
  }
  .brand-dot {
    width: 34px; height: 34px; border-radius: 50%;
  }
  .card--front .brand-dot { background: var(--paper); }
  .brand-name {
    font-weight: 700; font-size: 38px; letter-spacing: -0.5px;
  }
  .card--front .brand-name { color: var(--paper); }

  /* Back */
  .card--back { background: var(--paper); }
  .tree-wash {
    position: absolute; left: 500px; top: 10px; width: 190px; height: 230px;
    border-radius: 50% 50% 45% 45%;
    background: radial-gradient(circle at 50% 40%, var(--leaf-wash) 0%, rgba(232,241,214,0.4) 60%, rgba(255,255,255,0) 75%);
  }
  .shapes { position: absolute; inset: 0; }
  .back-brand {
    position: absolute; left: 60px; top: 80px;
    display: flex; align-items: center; gap: 10px;
  }
  .card--back .brand-dot { width: 26px; height: 26px; background: var(--green); }
  .card--back .brand-name { color: var(--ink); font-size: 30px; }
  .person {
    position: absolute; left: 175px; top: 160px;
    font-size: 13px; line-height: 22px; color: var(--ink-soft);
  }
  .person .role { padding-left: 24px; }
  .person .company { padding-left: 24px; font-weight: 600; color: var(--ink); }
  .contact {
    position: absolute; left: 210px; top: 280px;
    font-size: 13px; line-height: 24px; color: var(--ink-soft);
    list-style: none;
  }
  .contact li { display: flex; align-items: center; gap: 8px; }
  .contact strong { font-weight: 700; color: var(--ink); }
  .contact svg { flex: none; }
</style>
</head>
<body>
<main class="sheet">
  <section class="card card--front" aria-label="Card front">
    <span class="brand-dot"></span>
    <span class="brand-name">Kestrel Arc Solutions</span>
  </section>

  <section class="card card--back" aria-label="Card back">
    <div class="tree-wash" role="img" aria-label="Faint pastel tree illustration"></div>
    <svg class="shapes" width="700" height="400" viewBox="0 0 700 400" aria-hidden="true">
      <polygon points="330,170 380,110 700,110 700,170" fill="var(--green-light)"/>
      <polygon points="360,170 330,170 380,110 395,110" fill="var(--green)"/>
      <polygon points="0,276 150,276 120,304 0,304" fill="var(--green)"/>
    </svg>

    <div class="back-brand">
      <span class="brand-dot"></span>
      <span class="brand-name">Kestrel Arc Solutions</span>
    </div>

    <div class="person">
      <p class="name">Oliver Hastings</p>
      <p class="role">Director</p>
      <p class="company">Kestrel Arc Solutions</p>
    </div>

    <ul class="contact">
      <li>
        <svg width="12" height="14" viewBox="0 0 12 14"><path d="M6 0a5 5 0 0 0-5 5c0 4 5 9 5 9s5-5 5-9a5 5 0 0 0-5-5z" fill="var(--green)"/><circle cx="6" cy="5" r="2" fill="#fff"/></svg>
        <span><strong>Address:</strong> 14 Morrow Lane, Birmingham, B7 4QX</span>
      </li>
      <li>
        <svg width="12" height="12" viewBox="0 0 12 12"><circle cx="6" cy="6" r="6" fill="var(--green)"/><path d="M3.5 3.2l1.2-.4.8 1.7-.7.6c.4.9 1 1.5 1.9 1.9l.6-.7 1.7.8-.4 1.2c-3 .2-5.3-2.1-5.1-5.1z" fill="#fff"/></svg>
        <span><strong>Phone:</strong> 0845 217 6640</span>
      </li>
    </ul>
  </section>
</main>
</body>
</html>
```